Brightwell - Self Development Mobile App

Basic Instructions
1. please create an android app screen design for me, in figma, for my new app “Brightwell” based on this pencil drawing (Subjects.jpg)
2. Create the color pallet based on the colors of the logo (#fcd354 and #5dc9b7) and also add shades based on these colors based on material design.
3. the background should be white.
4. Use material design
Get Inspired by parlavox design and calmreed design
These are the directions i provided for the programmer on how this screen will work:
top bar:
back icon on left (show if you are in a category and press to go back one category)
name of the field in middle in bold
share icon for sharing the current subject on the right before the drop down menu
3 dot icon on the right (drop down menu)
2nd top bar:
fire icon on left for streak (how many days straight did you do a lesson)
star icon a bit after it (how many lessons did you pass)
circles section:
each category will get a section
each category will have a small star with a number that shows how many stars the user has from that category
each category will have an icon before it
under each category there will be circles for all the subjects under that category
scroll horizontally to see more subjects
each subject will have the amount stars gained from it (like the circles of the fields in the fields screen)
scroll down to see more fields with their subjects
note that the order of the subjects and categories should be based on the practial/spiritual score that the user has been assigned based on the initial wizard
More Notes
1. the scribbles in the circles under the following categories (Dreams, Sub-Concious, Feeling)) are just place filers. Please add example content based on the content in the circles that are under “Memory” category
2. There are more sections after Feeling so users should be able to scroll down to see more sections
3. There are more categories to the right so under each section
Final Thoughts
Maybe its better to have rounded cornered squares instead of circles. You choose what you think is best.
After you have created the Subjects screen and I like it, then I'll give you instructions for the other 5 screens.
general public, adults 18-80

```html
<!DOCTYPE html>
<html lang="en">
<head>
<meta charset="utf-8">
<title>Brightwell – App Screens</title>
<link href="https://fonts.googleapis.com/css2?family=Lato:wght@400;700&display=swap" rel="stylesheet">
<style>
:root{
  --teal:#5dc9b7;
  --teal-bar:#6fcfbd;
  --teal-deep:#2d6b63;
  --yellow:#fcd354;
  --star:#f7b500;
  --fire:#f4511e;
  --ink:#2f3433;
  --cream:#fffdf4;
  --bg:#ffffff;
}
*{box-sizing:border-box;margin:0;padding:0}
html,body{width:1200px;height:837px;overflow:hidden;background:var(--bg)}
body{font-family:'Lato',sans-serif;color:var(--ink)}
.stage{position:absolute;left:0;top:0;width:1433px;height:1000px;transform:scale(.8375);transform-origin:0 0}
.screen{position:absolute;width:414px;height:896px;overflow:hidden;
  background:linear-gradient(180deg,var(--cream) 0%,#fcf7de 30%,#d6e6bf 55%,#a3d9b6 72%,#6fcfbd 100%)}
.screen-fields{left:40px;top:48px}
.screen-mind{left:505px;top:52px}
.screen-wizard{left:969px;top:52px}
.app-bar{position:absolute;left:0;top:0;width:100%;height:46px;background:var(--teal-bar);
  border-radius:0 0 22px 22px;display:flex;align-items:center;justify-content:center;font-size:19px}
.app-bar .back{position:absolute;left:22px;top:14px}
.app-bar .actions{position:absolute;right:18px;top:11px;display:flex;gap:12px;align-items:center}
.stats{position:absolute;left:22px;right:18px;top:58px;height:42px}
.badge{position:absolute;top:0;display:flex;align-items:center;gap:10px;font-size:19px}
.badge .disc{width:40px;height:40px;border-radius:50%;background:#fff;box-shadow:0 1px 4px rgba(0,0,0,.12);
  display:flex;align-items:center;justify-content:center}
.badge-streak{left:0}
.badge-stars{right:0}
.tile{position:relative;width:118px;height:118px;background:var(--teal);border-radius:6px;
  text-align:center;font-size:17px}
.tile .icon{position:absolute;left:0;right:0;top:30px;display:flex;justify-content:center}
.tile .label{position:absolute;left:0;right:0;top:64px;white-space:nowrap}
.tile .score{position:absolute;left:12px;top:90px;font-size:17px;display:flex;align-items:center;gap:3px}
.field-grid{position:absolute;left:23px;top:233px;display:grid;grid-template-columns:repeat(3,118px);
  column-gap:9.5px;row-gap:13px}
.field-grid .label.large{font-size:20px}
.category{position:absolute;left:0;width:414px}
.category-title{position:absolute;left:21px;top:0;display:flex;align-items:center;gap:8px;font-size:19px}
.category-title .score{font-size:17px;display:flex;align-items:center;gap:2px}
.subject-row{position:absolute;left:22px;top:23px;display:grid;grid-template-columns:repeat(3,118px);column-gap:9.5px}
.subject-row .icon{top:18px}
.subject-row .label{top:46px}
.subject-row .label.lower{top:49px}
.scroll-arrow{position:absolute;top:70px}
.scroll-arrow.left{left:6px}
.scroll-arrow.right{left:401px}
.bottom-nav{position:absolute;left:0;bottom:0;width:100%;height:79px;background:var(--yellow);
  border-radius:30px 30px 0 0;display:grid;grid-template-columns:repeat(3,1fr);padding:0 10px}
.nav-item{display:flex;flex-direction:column;align-items:center;justify-content:center;gap:4px;font-size:17px}
.progress{position:absolute;left:22px;top:88px;width:372px;height:21px;border-radius:11px;background:var(--teal)}
.progress-fill{position:absolute;left:13px;top:7px;width:166px;height:7px;border-radius:4px;background:var(--teal-deep)}
.wizard-step{position:absolute;left:0;right:0;top:128px;text-align:center;font-size:19px}
.wizard-prompt{position:absolute;left:22px;right:26px;top:180px;font-size:18.5px;line-height:28px}
.choice-grid{position:absolute;left:22px;top:290px;display:grid;grid-template-columns:repeat(3,118px);
  column-gap:9.5px;row-gap:15px}
.choice-grid .label{top:66px}
.wizard-footer{position:absolute;left:22px;right:24px;top:730px;height:34px}
.wizard-footer .badge{gap:8px}
.wizard-footer .disc{width:32px;height:32px}
.mic{position:absolute;right:0;top:4px}
</style>
</head>
<body>
<svg width="0" height="0" style="position:absolute">
  <defs>
    <symbol id="i-back" viewBox="0 0 24 24"><path d="M15 5l-7 7 7 7" fill="none" stroke="#222" stroke-width="2.4" stroke-linecap="round" stroke-linejoin="round"/></symbol>
    <symbol id="i-next" viewBox="0 0 24 24"><path d="M9 5l7 7-7 7" fill="none" stroke="#222" stroke-width="2.4" stroke-linecap="round" stroke-linejoin="round"/></symbol>
    <symbol id="i-share" viewBox="0 0 24 24"><g fill="#222"><circle cx="18" cy="5" r="3"/><circle cx="6" cy="12" r="3"/><circle cx="18" cy="19" r="3"/></g><path d="M18 5L6 12l12 7" fill="none" stroke="#222" stroke-width="2"/></symbol>
    <symbol id="i-more" viewBox="0 0 8 24"><g fill="#222"><circle cx="4" cy="4" r="2.4"/><circle cx="4" cy="12" r="2.4"/><circle cx="4" cy="20" r="2.4"/></g></symbol>
    <symbol id="i-fire" viewBox="0 0 24 24"><path d="M12 2c1 4 6 6 6 12a6 6 0 0 1-12 0c0-3 2-5 3-6 0 2 1 3 2 3-1-3 0-6 1-9z" fill="var(--fire)"/><path d="M12 12c1 2 3 3 3 5a3 3 0 0 1-6 0c0-2 2-3 3-5z" fill="var(--yellow)"/></symbol>
    <symbol id="i-star" viewBox="0 0 24 24"><path d="M12 2l3 6.5 7 .8-5.2 4.8 1.5 7L12 17.6 5.7 21.1l1.5-7L2 9.3l7-.8z" fill="var(--star)"/></symbol>
    <symbol id="i-head" viewBox="0 0 24 24"><path d="M12 2a8 8 0 0 0-8 8c0 2 .5 3 1.5 4.5L5 22h9v-3h3a2 2 0 0 0 2-2v-3l2-1-2-3a8 8 0 0 0-7-8z" fill="#333"/><path d="M8 8c1-2 4-3 6-1M9 11c1 1 3 1 4 0M11 5v4" stroke="var(--teal)" stroke-width="1.3" fill="none"/></symbol>
    <symbol id="i-thumb" viewBox="0 0 24 24"><circle cx="12" cy="12" r="10" fill="none" stroke="#333" stroke-width="2"/><path d="M8 11h2v6H8zM11 11l2-4c1 0 1.5.6 1.3 1.6L14 10h2.5c.8 0 1.3.7 1.1 1.4l-1.2 4.6c-.2.6-.7 1-1.3 1H11z" fill="#333"/></symbol>
    <symbol id="i-run" viewBox="0 0 24 24"><circle cx="12" cy="12" r="10" fill="none" stroke="#333" stroke-width="1.6" stroke-dasharray="40 8"/><circle cx="13" cy="6" r="1.7" fill="#333"/><path d="M12 9l-3 3 2 2-2 4M12 9l2 4 3 1M12 14l3 4" fill="none" stroke="#333" stroke-width="1.8" stroke-linecap="round"/></symbol>
    <symbol id="i-hobby" viewBox="0 0 24 24"><circle cx="12" cy="9" r="5" fill="#333"/><path d="M6 22c0-4 3-6 6-6s6 2 6 6z" fill="#333"/><g fill="#333"><circle cx="4" cy="6" r="1.8"/><circle cx="20" cy="6" r="1.8"/><circle cx="4" cy="14" r="1.8"/><circle cx="20" cy="14" r="1.8"/><circle cx="12" cy="2" r="1.5"/></g></symbol>
    <symbol id="i-person" viewBox="0 0 24 24"><circle cx="12" cy="7" r="5" fill="#333"/><path d="M3 23c0-6 4-9 9-9s9 3 9 9z" fill="#333"/></symbol>
    <symbol id="i-finance" viewBox="0 0 24 24"><circle cx="14" cy="7" r="5" fill="#333"/><path d="M14 4v6M12.5 5.5h2.5a1 1 0 0 1 0 2h-2a1 1 0 0 0 0 2h2.5" stroke="var(--teal)" stroke-width="1.2" fill="none"/><path d="M2 15h4l3 2h5a1.5 1.5 0 0 1 0 3H9M14 19l5-3c1-.5 2 .5 1.5 1.3L15 22H2z" fill="#333"/></symbol>
    <symbol id="i-yoga" viewBox="0 0 24 24"><circle cx="12" cy="4" r="2.3" fill="#333"/><path d="M12 7c-2 0-3 1-3 3v3l-4 1M12 7c2 0 3 1 3 3v3l4 1M6 18c2-2 4-2 6-2s4 0 6 2M3 21h18" fill="none" stroke="#333" stroke-width="2" stroke-linecap="round"/><path d="M9 13h6v3H9z" fill="#333"/></symbol>
    <symbol id="i-social" viewBox="0 0 24 24"><g fill="#333"><circle cx="8" cy="7" r="4"/><circle cx="16" cy="13" r="4"/><circle cx="8" cy="18" r="3"/><circle cx="18" cy="4" r="2"/><circle cx="19" cy="20" r="2"/></g></symbol>
    <symbol id="i-pro" viewBox="0 0 24 24"><circle cx="13" cy="5" r="3.5" fill="#333"/><path d="M6 23v-8c0-3 3-5 7-5s7 2 7 5v8z" fill="#333"/><path d="M3 14l5-1v5c0 2-2 4-2.5 4S3 20 3 18z" fill="#333" stroke="var(--teal)" stroke-width="1"/></symbol>
    <symbol id="i-history" viewBox="0 0 24 24"><circle cx="13" cy="12" r="8.5" fill="none" stroke="#333" stroke-width="2"/><path d="M13 7v5l3 2" stroke="#333" stroke-width="2" fill="none" stroke-linecap="round"/><path d="M1 10l3.5 3L8 10z" fill="#333"/></symbol>
    <symbol id="i-user" viewBox="0 0 24 24"><circle cx="12" cy="12" r="9.5" fill="none" stroke="#333" stroke-width="1.8"/><circle cx="12" cy="10" r="3.2" fill="none" stroke="#333" stroke-width="1.8"/><path d="M6.5 18.5c1.5-2 3.3-3 5.5-3s4 1 5.5 3" fill="none" stroke="#333" stroke-width="1.8"/></symbol>
    <symbol id="i-one" viewBox="0 0 24 24"><circle cx="12" cy="12" r="10" fill="#333"/><path d="M10 8l3-2v12" stroke="var(--teal)" stroke-width="2.2" fill="none"/></symbol>
    <symbol id="i-idea" viewBox="0 0 24 24"><path d="M11 4a7 7 0 0 0-7 7c0 2 .5 3 1.5 4.5L5 22h8v-3h3a2 2 0 0 0 2-2v-2l2-1-2-3a7 7 0 0 0-7-7z" fill="#333"/><g stroke="#333" stroke-width="1.4"><path d="M19 1v3M22 4h-2M16 2l1 2"/></g><circle cx="11" cy="10" r="2.5" fill="#fff"/></symbol>
    <symbol id="i-cloud" viewBox="0 0 24 24"><path d="M6 17a4 4 0 0 1 0-8 6 6 0 0 1 11-1 4.5 4.5 0 0 1 1 9z" fill="#333"/><circle cx="8" cy="20" r="1.5" fill="#333"/><circle cx="4.5" cy="22" r="1" fill="#333"/></symbol>
    <symbol id="i-pot" viewBox="0 0 24 24"><path d="M4 11h16l-2 10H6z" fill="#333"/><path d="M8 9l-2-6M12 9V2M16 9l2-6M10 9l-1-4M14 9l1-4" stroke="#333" stroke-width="1.6"/></symbol>
    <symbol id="i-faces" viewBox="0 0 24 24"><circle cx="8" cy="15" r="7" fill="#333"/><circle cx="17" cy="7" r="6" fill="none" stroke="#333" stroke-width="1.8"/><path d="M14.5 8.5c1.5 1.5 3.5 1.5 5 0" stroke="#333" stroke-width="1.5" fill="none"/><path d="M5 18c2-1.5 4-1.5 6 0" stroke="#fff" stroke-width="1.5" fill="none"/></symbol>
    <symbol id="i-books" viewBox="0 0 24 24"><g fill="#333"><rect x="4" y="18" width="17" height="4" rx="1"/><rect x="3" y="12.5" width="17" height="4" rx="1"/><rect x="5" y="7" width="16" height="4" rx="1"/><path d="M4 4l8-3 8 3-8 2z"/></g><g stroke="var(--teal)" stroke-width=".9"><path d="M6 20h13M5 14.5h13M7 9h12"/></g></symbol>
    <symbol id="i-figure" viewBox="0 0 24 24"><circle cx="12" cy="3" r="2.3" fill="#333"/><path d="M9 7h6l1 8h-2l-.5 8h-3L10 15H8z" fill="#333"/></symbol>
    <symbol id="i-mic" viewBox="0 0 24 24"><rect x="8.5" y="2" width="7" height="13" rx="3.5" fill="#222"/><path d="M5.5 11a6.5 6.5 0 0 0 13 0M12 17.5V22M8.5 22h7" fill="none" stroke="#222" stroke-width="2"/></symbol>
    <symbol id="i-group" viewBox="0 0 24 24"><g fill="#333"><circle cx="6" cy="8" r="2.5"/><circle cx="12" cy="7" r="2.8"/><circle cx="18" cy="8" r="2.5"/><path d="M2 18c0-3 2-5 4-5s3 1 3 1v4zM7 19c0-4 2-6 5-6s5 2 5 6zM22 18c0-3-2-5-4-5s-3 1-3 1v4z"/></g></symbol>
    <symbol id="i-compass" viewBox="0 0 24 24"><circle cx="12" cy="12" r="10" fill="#333"/><path d="M16 8l-2.5 5.5L8 16l2.5-5.5z" fill="var(--yellow)"/></symbol>
    <symbol id="i-account" viewBox="0 0 24 24"><circle cx="12" cy="12" r="10" fill="none" stroke="#333" stroke-width="2"/><circle cx="12" cy="9.5" r="3.5" fill="#333"/><path d="M6 18.5c1.5-2.5 3.5-3.5 6-3.5s4.5 1 6 3.5" fill="#333"/></symbol>
  </defs>
</svg>

<main class="stage">

  <!-- Fields screen -->
  <section class="screen screen-fields">
    <header class="app-bar">
      <svg class="back" width="18" height="18"><use href="#i-back"/></svg>
      <div class="actions"><svg width="18" height="18"><use href="#i-share"/></svg><svg width="7" height="22"><use href="#i-more"/></svg></div>
    </header>
    <div class="stats">
      <div class="badge badge-streak"><span class="disc"><svg width="26" height="26"><use href="#i-fire"/></svg></span>2</div>
      <div class="badge badge-stars"><span class="disc"><svg width="32" height="32"><use href="#i-star"/></svg></span>34</div>
    </div>
    <div class="field-grid">
      <div class="tile"><span class="icon"><svg width="36" height="36"><use href="#i-head"/></svg></span><span class="label">Mind</span></div>
      <div class="tile"><span class="icon"><svg width="34" height="34"><use href="#i-thumb"/></svg></span><span class="label">Recommend</span><span class="score"><svg width="16" height="16"><use href="#i-star"/></svg>4</span></div>
      <div class="tile"><span class="icon"><svg width="34" height="34"><use href="#i-run"/></svg></span><span class="label">Body</span><span class="score"><svg width="16" height="16"><use href="#i-star"/></svg>4</span></div>
      <div class="tile"><span class="icon"><svg width="32" height="32"><use href="#i-hobby"/></svg></span><span class="label large">Hobbies</span><span class="score" style="left:10px"><svg width="16" height="16"><use href="#i-star"/></svg>4</span></div>
      <div class="tile"><span class="icon"><svg width="34" height="34"><use href="#i-person"/></svg></span><span class="label large">Me</span></div>
      <div class="tile"><span class="icon"><svg width="34" height="34"><use href="#i-finance"/></svg></span><span class="label">Finance</span></div>
      <div class="tile"><span class="icon"><svg width="34" height="34"><use href="#i-yoga"/></svg></span><span class="label">Spiritual</span></div>
      <div class="tile"><span class="icon"><svg width="34" height="34"><use href="#i-social"/></svg></span><span class="label">Social</span><span class="score"><svg width="16" height="16"><use href="#i-star"/></svg>4</span></div>
      <div class="tile"><span class="icon"><svg width="34" height="34"><use href="#i-pro"/></svg></span><span class="label">Proffessional</span></div>
    </div>
    <nav class="bottom-nav">
      <div class="nav-item"><svg width="18" height="18"><use href="#i-group"/></svg>Fields</div>
      <div class="nav-item"><svg width="20" height="20"><use href="#i-compass"/></svg>Explore</div>
      <div class="nav-item"><svg width="20" height="20"><use href="#i-account"/></svg>Account</div>
    </nav>
  </section>

  <!-- Mind screen -->
  <section class="screen screen-mind">
    <header class="app-bar">
      <svg class="back" width="18" height="18"><use href="#i-back"/></svg>Mind
      <div class="actions"><svg width="18" height="18"><use href="#i-share"/></svg><svg width="7" height="22"><use href="#i-more"/></svg></div>
    </header>
    <div class="stats">
      <div class="badge badge-streak"><span class="disc"><svg width="26" height="26"><use href="#i-fire"/></svg></span>2</div>
      <div class="badge badge-stars"><span class="disc"><svg width="32" height="32"><use href="#i-star"/></svg></span>34</div>
    </div>

    <div class="category" style="top:120px">
      <h2 class="category-title" style="font-weight:400">Memory <svg width="24" height="24"><use href="#i-idea"/></svg><span class="score"><svg width="15" height="15"><use href="#i-star"/></svg>7</span></h2>
      <svg class="scroll-arrow left" width="12" height="16"><use href="#i-back"/></svg>
      <div class="subject-row">
        <div class="tile"><span class="icon"><svg width="30" height="30"><use href="#i-history"/></svg></span><span class="label">Basic Memory</span><span class="score"><svg width="15" height="15"><use href="#i-star"/></svg>2</span></div>
        <div class="tile"><span class="icon"><svg width="26" height="26"><use href="#i-user"/></svg></span><span class="label lower">Name</span><span class="score"><svg width="15" height="15"><use href="#i-star"/></svg>1</span></div>
        <div class="tile"><span class="icon"><svg width="25" height="25"><use href="#i-one"/></svg></span><span class="label lower">Number</span><span class="score"><svg width="15" height="15"><use href="#i-star"/></svg>4</span></div>
      </div>
      <svg class="scroll-arrow right" width="12" height="16"><use href="#i-next"/></svg>
    </div>

    <div class="category" style="top:290px">
      <h2 class="category-title" style="font-weight:400">Dreams <svg width="24" height="24"><use href="#i-cloud"/></svg><span class="score"><svg width="15" height="15"><use href="#i-star"/></svg>3</span></h2>
      <svg class="scroll-arrow left" width="12" height="16"><use href="#i-back"/></svg>
      <div class="subject-row">
        <div class="tile"><span class="icon"><svg width="30" height="30"><use href="#i-history"/></svg></span><span class="label">Basic Memory</span><span class="score"><svg width="15" height="15"><use href="#i-star"/></svg>2</span></div>
        <div class="tile"><span class="icon"><svg width="26" height="26"><use href="#i-user"/></svg></span><span class="label lower">Name</span><span class="score"><svg width="15" height="15"><use href="#i-star"/></svg>1</span></div>
        <div class="tile"><span class="icon"><svg width="25" height="25"><use href="#i-one"/></svg></span><span class="label lower">Number</span><span class="score"><svg width="15" height="15"><use href="#i-star"/></svg>4</span></div>
      </div>
      <svg class="scroll-arrow right" width="12" height="16"><use href="#i-next"/></svg>
    </div>

    <div class="category" style="top:460px">
      <h2 class="category-title" style="font-weight:400">Sub Concious <svg width="22" height="22"><use href="#i-pot"/></svg></h2>
      <svg class="scroll-arrow left" width="12" height="16"><use href="#i-back"/></svg>
      <div class="subject-row">
        <div class="tile"><span class="icon"><svg width="30" height="30"><use href="#i-history"/></svg></span><span class="label">Basic Memory</span><span class="score"><svg width="15" height="15"><use href="#i-star"/></svg>2</span></div>
        <div class="tile"><span class="icon"><svg width="26" height="26"><use href="#i-user"/></svg></span><span class="label lower">Name</span><span class="score"><svg width="15" height="15"><use href="#i-star"/></svg>1</span></div>
        <div class="tile"><span class="icon"><svg width="25" height="25"><use href="#i-one"/></svg></span><span class="label lower">Number</span><span class="score"><svg width="15" height="15"><use href="#i-star"/></svg>4</span></div>
      </div>
      <svg class="scroll-arrow right" width="12" height="16"><use href="#i-next"/></svg>
    </div>

    <div class="category" style="top:630px">
      <h2 class="category-title" style="font-weight:400">Feeling <svg width="26" height="26"><use href="#i-faces"/></svg></h2>
      <svg class="scroll-arrow left" width="12" height="16"><use href="#i-back"/></svg>
      <div class="subject-row">
        <div class="tile"><span class="icon"><svg width="30" height="30"><use href="#i-history"/></svg></span><span class="label">Basic Memory</span><span class="score"><svg width="15" height="15"><use href="#i-star"/></svg>2</span></div>
        <div class="tile"><span class="icon"><svg width="26" height="26"><use href="#i-user"/></svg></span><span class="label lower">Name</span><span class="score"><svg width="15" height="15"><use href="#i-star"/></svg>1</span></div>
        <div class="tile"><span class="icon"><svg width="25" height="25"><use href="#i-one"/></svg></span><span class="label lower">Number</span><span class="score"><svg width="15" height="15"><use href="#i-star"/></svg>4</span></div>
      </div>
      <svg class="scroll-arrow right" width="12" height="16"><use href="#i-next"/></svg>
    </div>

    <nav class="bottom-nav">
      <div class="nav-item"><svg width="18" height="18"><use href="#i-group"/></svg>Fields</div>
      <div class="nav-item"><svg width="20" height="20"><use href="#i-compass"/></svg>Explore</div>
      <div class="nav-item"><svg width="20" height="20"><use href="#i-account"/></svg>Account</div>
    </nav>
  </section>

  <!-- Wizard screen -->
  <section class="screen screen-wizard">
    <header class="app-bar">
      <svg class="back" width="18" height="18"><use href="#i-back"/></svg>Wizard
      <div class="actions"><svg width="18" height="18"><use href="#i-share"/></svg><svg width="7" height="22"><use href="#i-more"/></svg></div>
    </header>
    <div class="progress"><div class="progress-fill"></div></div>
    <p class="wizard-step">Brightwell</p>
    <p class="wizard-prompt">Please choose three subjuct that intevest you most</p>
    <div class="choice-grid">
      <div class="tile"><span class="icon"><svg width="36" height="36"><use href="#i-head"/></svg></span><span class="label">Mind</span></div>
      <div class="tile"><span class="icon"><svg width="34" height="34"><use href="#i-books"/></svg></span><span class="label" style="top:64px">Subject</span></div>
      <div class="tile"><span class="icon"><svg width="32" height="32"><use href="#i-figure"/></svg></span><span class="label">Body</span></div>
      <div class="tile"><span class="icon"><svg width="36" height="36"><use href="#i-head"/></svg></span><span class="label">Mind</span></div>
      <div class="tile"><span class="icon"><svg width="34" height="34"><use href="#i-books"/></svg></span><span class="label" style="top:64px">Subject</span></div>
      <div class="tile"><span class="icon"><svg width="32" height="32"><use href="#i-figure"/></svg></span><span class="label">Body</span></div>
      <div class="tile"><span class="icon"><svg width="36" height="36"><use href="#i-head"/></svg></span><span class="label">Mind</span></div>
      <div class="tile"><span class="icon"><svg width="34" height="34"><use href="#i-books"/></svg></span><span class="label" style="top:64px">Subject</span></div>
      <div class="tile"><span class="icon"><svg width="32" height="32"><use href="#i-figure"/></svg></span><span class="label">Body</span></div>
    </div>
    <div class="wizard-footer">
      <div class="badge badge-streak"><span class="disc"><svg width="24" height="24"><use href="#i-star"/></svg></span>9</div>
      <svg class="mic" width="22" height="26"><use href="#i-mic"/></svg>
    </div>
  </section>

</main>
</body>
</html>
```